Australian IT Company requires Business Card Design

Bluepeak is an Australian company that specialises in IT consulting & support, software development, project management, network services.

We have been in business for 15 years.

* We require a business card with the following on it:
Logo
Address
Contact Details
Space for staff name, title & mobile number

Industry/Entity Type

Software

```html
<!DOCTYPE html>
<html lang="en">
<head>
<meta charset="utf-8">
<title>Bluepeak Business Card</title>
<link rel="stylesheet" href="https://fonts.googleapis.com/css2?family=Mulish:wght@400;600;700&display=swap">
<style>
  :root {
    --page-bg: #e9e7e4;
    --card-bg: #f4f5f6;
    --card-edge: #d5d7da;
    --navy: #2f4a6b;
    --navy-deep: #233a57;
    --ink: #4a4f57;
    --ink-soft: #5b6068;
  }
  * { margin: 0; padding: 0; box-sizing: border-box; }
  html, body {
    width: 1200px;
    height: 970px;
    overflow: hidden;
    background: var(--page-bg);
    font-family: "Mulish", sans-serif;
  }
  .business-card {
    position: absolute;
    left: 60px;
    top: 185px;
    width: 1080px;
    height: 600px;
    background: var(--card-bg);
    border: 1px solid var(--card-edge);
    overflow: hidden;
  }
  .brand-name {
    position: absolute;
    left: 63px;
    top: 74px;
    font-size: 56px;
    font-weight: 600;
    letter-spacing: 1px;
    color: var(--navy);
    line-height: 1;
  }
  .brand-tagline {
    position: absolute;
    left: 65px;
    top: 141px;
    font-size: 17px;
    letter-spacing: 4.2px;
    color: var(--ink-soft);
    text-transform: uppercase;
    white-space: nowrap;
  }
  .staff-name {
    position: absolute;
    left: 63px;
    top: 232px;
    font-size: 29px;
    font-weight: 700;
    color: var(--navy);
  }
  .staff-title {
    position: absolute;
    left: 63px;
    top: 268px;
    font-size: 24px;
    color: var(--ink);
  }
  .contact-list {
    position: absolute;
    left: 63px;
    top: 321px;
    list-style: none;
  }
  .contact-item {
    display: flex;
    align-items: center;
    height: 33px;
    font-size: 24px;
    color: var(--ink);
    white-space: nowrap;
  }
  .contact-icon {
    width: 22px;
    height: 22px;
    margin-right: 12px;
    fill: var(--ink);
  }
  .address {
    position: absolute;
    left: 63px;
    top: 444px;
    font-size: 24px;
    line-height: 31px;
    font-style: normal;
    color: var(--ink);
  }
  .decor-blocks {
    position: absolute;
    left: 0;
    top: 0;
    width: 1080px;
    height: 600px;
  }
  .block { fill: var(--navy); }
  .block-deep { fill: var(--navy-deep); }
</style>
</head>
<body>
  <div class="business-card">
    <svg class="decor-blocks" viewBox="0 0 1080 600" aria-hidden="true">
      <rect class="block" x="481" y="204" width="69" height="60"/>
      <rect class="block" x="547" y="362" width="97" height="85"/>
      <rect class="block" x="751" y="89" width="157" height="136"/>
      <rect class="block-deep" x="672" y="246" width="408" height="354"/>
    </svg>

    <div class="brand-name">BLUEPEAK</div>
    <div class="brand-tagline">Smart IT Solutions For Business</div>

    <div class="staff-name">Daniel Whitford</div>
    <div class="staff-title">Managing Director</div>

    <ul class="contact-list">
      <li class="contact-item">
        <svg class="contact-icon" viewBox="0 0 24 24"><path d="M6.6 10.8a15 15 0 0 0 6.6 6.6l2.2-2.2a1 1 0 0 1 1-.25 11.4 11.4 0 0 0 3.6.57 1 1 0 0 1 1 1V20a1 1 0 0 1-1 1A17 17 0 0 1 3 4a1 1 0 0 1 1-1h3.5a1 1 0 0 1 1 1c0 1.25.2 2.45.57 3.6a1 1 0 0 1-.25 1z"/></svg>
        +61 3 9555 0182
      </li>
      <li class="contact-item">
        <svg class="contact-icon" viewBox="0 0 24 24"><path d="M3 5h18v14H3z M4.5 6.5v.3l7.5 5.4 7.5-5.4v-.3z M4.5 8.6v8.9h15V8.6L12 14z" fill-rule="evenodd"/></svg>
        daniel@bluepeak.net.au
      </li>
      <li class="contact-item">
        <svg class="contact-icon" viewBox="0 0 24 24"><path d="M12 2a10 10 0 1 0 0 20 10 10 0 0 0 0-20zm6.9 6h-2.9a15 15 0 0 0-1.3-3.6A8 8 0 0 1 18.9 8zM12 4a13 13 0 0 1 1.9 4h-3.8A13 13 0 0 1 12 4zM4.3 14a8 8 0 0 1 0-4h3.4a16 16 0 0 0 0 4zm.8 2h2.9a15 15 0 0 0 1.3 3.6A8 8 0 0 1 5.1 16zM8 8H5.1a8 8 0 0 1 4.2-3.6A15 15 0 0 0 8 8zm4 12a13 13 0 0 1-1.9-4h3.8A13 13 0 0 1 12 20zm2.3-6H9.7a14 14 0 0 1 0-4h4.6a14 14 0 0 1 0 4zm.4 5.6A15 15 0 0 0 16 16h2.9a8 8 0 0 1-4.2 3.6zM16.3 14a16 16 0 0 0 0-4h3.4a8 8 0 0 1 0 4z"/></svg>
        www.bluepeak.net.au
      </li>
    </ul>

    <address class="address">
      14 Ridge Lane<br>
      Harbour House 3<br>
      Kew Vic 3101
    </address>
  </div>
</body>
</html>
```